Velvora Beauty Sensitive Skin Intimate Shave Cream

We need a label/package design for a female shave cream. Our brand is Velvora Beauty and we manufacturer luxuriously sexy female intimate items. We are looking for sexy packaging to really get our brand out there. I have included in attachments, all of the files including font, logo, size requirements and verbage requirements. On the file "shave-cream-requirements" please use to format for size. Also on that file, I need the "must have" verbage from my project brief laid out exactly the same. The name of the product is Velvora Beauty Classic Silken Intimate Shave Cream
Target Market(s)
Females who like luxury and feeling sexy
Industry/Entity Type
Manufacturer
Requirements
Must have
- Must have my velvora beauty logo. The scent for this cream is called "silken classic" Please put that one the label. Also the actual scent is "an array of light florals with a hint of baby powder" please put that in small letters on back of the label
- Must be Label Dimensions: 6.25h X 7.375w
- Must say "Intimate Shave Cream for Her".
- Must say - Fill Weight: 16 Fl. Oz. (480ml) ℮
- must say - Suggested use: Apply intimate shave cream where desired and glide razor over skin for smooth results
- Must say - Ingredient Deck:
- Water (Eau/Aqua), Cetyl Alcohol, Cetrimonium Bromide, Stearyl Alcohol, Hydroxyethylcellulose, Glyceryl Stearate, PEG-100 Stearate, PEG-60 Lanolin, Simmondsia Chinensis (Jojoba) Seed Oil, Hydrolyzed Keratin, Panthenol, Allantoin, Phenoxyethanol, Methylisothiazolinone, Sodium Hydroxide, Fragrance (Parfum)
- Must say these cautions:
- Recommend Cautions:
- Do Not Use if You have a Known Hypersensitivity (Allergy) to Any of the Ingredients
- If Irritation Occurs, Discontinue Use
- If Eye Contact Occurs, Rinse with Water to Remove
- Keep Out of Reach of Children
- Must say : Specially formulated with skin soothing ingredients to provide a smooth and effortless shave.
- Protects and nourishes from irritation and razor cuts
- Helps prevent embarrassing shave rashes and ingrown hairs.
- Designed for sensitive and intimate skin. Perfect for intimate areas, legs, underarms, face, and body.
- Enhanced with hair and skin moisturizing agents.
- Can also be used to condition skin and hair after shampoo.
- Must have UPC (included) and part number:VK584731 in small writing on the back of the label.
Should not have
- cheap looking designs and logos

```html
<!DOCTYPE html>
<html lang="en">
<head>
<meta charset="utf-8">
<title>Velvora Beauty Classic Silken Intimate Shave Cream – Label</title>
<link href="https://fonts.googleapis.com/css2?family=Open+Sans:wght@400;600;700&family=Josefin+Sans:wght@300&family=Raleway:wght@200&family=Lobster+Two:ital,wght@1,700&family=Arimo&display=swap" rel="stylesheet">
<style>
  :root {
    --ink: #111112;
    --pink: #d8398a;
    --pink-deep: #7a1747;
    --title-pink: #dc4f98;
    --silver-light: #e6e6e6;
    --silver: #b9b9b9;
    --silver-dark: #8e8e8e;
    --text-light: #ffffff;
    --logo-silver: #cfcfcf;
    --page: #ffffff;
  }
  * { margin: 0; padding: 0; box-sizing: border-box; }
  html, body { width: 1200px; height: 786px; overflow: hidden; background: var(--page); }
  .label {
    position: absolute; left: 50px; top: 56px;
    width: 1100px; height: 674px;
    font-family: "Open Sans", Arial, sans-serif; color: var(--text-light);
  }
  .label-art { position: absolute; inset: 0; }
  .block { position: absolute; font-size: 12px; line-height: 16.5px; }
  .block h3 { font-size: 12px; font-weight: 700; line-height: 16.5px; }

  .usage { left: 22px; top: 58px; width: 180px; }
  .ingredients { left: 22px; top: 132px; width: 182px; font-size: 10.5px; line-height: 15px; }
  .ingredients h3 { font-size: 12px; margin-bottom: 3px; }
  .cautions { left: 22px; top: 396px; width: 196px; font-size: 11.5px; }

  .claims { position: absolute; left: 220px; top: 0; width: 46px; height: 674px; }
  .claim { position: absolute; left: 0; width: 46px; text-align: center; font-size: 6.5px; line-height: 8px; }
  .claim svg { display: block; margin: 0 auto 4px; }

  .brand-name, .brand-sub {
    position: absolute; writing-mode: vertical-rl; transform: rotate(180deg);
    font-family: "Raleway", Arial, sans-serif; font-weight: 200; color: var(--logo-silver);
    white-space: nowrap;
  }
  .brand-name { left: 372px; top: 92px; font-size: 70px; letter-spacing: 17px; line-height: 80px; }
  .brand-sub { left: 494px; top: 258px; font-size: 26px; letter-spacing: 14px; line-height: 30px; }

  .product { position: absolute; left: 540px; top: 180px; width: 160px; text-align: center; }
  .product-type { font-family: "Josefin Sans", Arial, sans-serif; font-weight: 300; color: var(--title-pink); font-size: 31px; letter-spacing: 1px; line-height: 36px; }
  .product-desc { font-family: "Josefin Sans", Arial, sans-serif; font-weight: 300; font-size: 15px; line-height: 30px; margin-top: 6px; }
  .scent-name {
    font-family: "Lobster Two", cursive; font-style: italic; font-weight: 700;
    font-size: 37px; line-height: 40px; margin-top: 14px;
    background: linear-gradient(180deg, #ffffff 0%, #bdbdbd 55%, #8a8a8a 100%);
    -webkit-background-clip: text; background-clip: text; color: transparent;
  }
  .fill-weight { position: absolute; left: 480px; top: 603px; width: 240px; text-align: center; font-size: 14px; }

  .benefits { right: 28px; top: 52px; width: 176px; text-align: right; font-size: 12px; line-height: 16.5px; }
  .directions { right: 28px; top: 354px; width: 150px; text-align: right; font-size: 12px; }
  .scent-note { right: 28px; top: 450px; width: 120px; text-align: right; font-size: 12px; }
  .part-info { position: absolute; left: 930px; top: 548px; width: 110px; text-align: center; font-family: "Arimo", Arial, sans-serif; font-size: 15px; line-height: 16px; }
</style>
</head>
<body>
<main class="label">
  <svg class="label-art" width="1100" height="674" viewBox="0 0 1100 674" aria-hidden="true">
    <defs>
      <linearGradient id="side-panel" x1="0" y1="0" x2="0" y2="1">
        <stop offset="0" stop-color="#111112"/>
        <stop offset="0.18" stop-color="#2a0d1c"/>
        <stop offset="0.42" stop-color="#d8398a"/>
        <stop offset="0.58" stop-color="#c9347f"/>
        <stop offset="0.8" stop-color="#3b1027"/>
        <stop offset="1" stop-color="#111112"/>
      </linearGradient>
      <linearGradient id="silver-band" x1="0" y1="0" x2="0" y2="1">
        <stop offset="0" stop-color="#8e8e8e"/>
        <stop offset="0.5" stop-color="#e6e6e6"/>
        <stop offset="1" stop-color="#9d9d9d"/>
      </linearGradient>
    </defs>
    <rect x="0" y="20" width="1100" height="634" fill="url(#side-panel)"/>
    <path d="M275,20 Q250,337 275,654 L825,654 Q850,337 825,20 Z" fill="#111112"/>
    <rect x="0" y="0" width="1100" height="20" fill="url(#silver-band)"/>
    <rect x="0" y="654" width="1100" height="20" fill="url(#silver-band)"/>
  </svg>

  <section class="block usage">
    <h3>Suggested use:</h3>
    <p>Apply intimate shave cream where desired and glide razor over skin for smooth results</p>
  </section>

  <section class="block ingredients">
    <h3>Ingredient :</h3>
    <p>Water (Eau/Aqua), Cetyl Alcohol, Cetrimonium Bromide, Stearyl Alcohol, Hydroxyethylcellulose, Glyceryl Stearate, PEG-100 Stearate, PEG-60 Lanolin, Simmondsia Chinensis (Jojoba) Seed Oil, Hydrolyzed Keratin, Panthenol, Allantoin, Phenoxyethanol, Methylisothiazolinone, Sodium Hydroxide, Fragrance (Parfum)</p>
  </section>

  <section class="block cautions">
    <h3>Recommend Cautions:</h3>
    <p>Do Not Use if You have a Known Hypersensitivity (Allergy) to Any of the Ingredients.</p>
    <p>If Irritation Occurs, Discontinue Use.</p>
    <p>If Eye Contact Occurs, Rinse with Water to Remove.</p>
    <p>Keep Out of Reach of Children.</p>
  </section>

  <ul class="claims">
    <li class="claim" style="top:58px"><svg width="44" height="24" viewBox="0 0 44 24"><rect x="1" y="1" width="42" height="22" fill="none" stroke="#fff" stroke-width="1.5"/></svg>Made in USA</li>
    <li class="claim" style="top:146px"><svg width="34" height="34" viewBox="0 0 34 34"><circle cx="17" cy="17" r="15" fill="none" stroke="#fff" stroke-width="1.5"/></svg>No Animal Testing</li>
    <li class="claim" style="top:250px"><svg width="34" height="34" viewBox="0 0 34 34"><circle cx="17" cy="17" r="15" fill="none" stroke="#fff" stroke-width="1.5"/></svg>Sugar-Free</li>
    <li class="claim" style="top:366px"><svg width="34" height="34" viewBox="0 0 34 34"><circle cx="17" cy="17" r="15" fill="none" stroke="#fff" stroke-width="1.5"/></svg>Safe For All Skin Types</li>
    <li class="claim" style="top:476px"><svg width="34" height="34" viewBox="0 0 34 34"><circle cx="17" cy="17" r="15" fill="none" stroke="#fff" stroke-width="1.5"/></svg>Paraben-Free</li>
    <li class="claim" style="top:580px"><svg width="34" height="34" viewBox="0 0 34 34"><circle cx="17" cy="17" r="15" fill="none" stroke="#fff" stroke-width="1.5"/></svg>Sulfate-Free</li>
  </ul>

  <h1 class="brand-name">VELVORA</h1>
  <p class="brand-sub">BEAUTY</p>

  <section class="product">
    <h2 class="product-type">INTIMATE</h2>
    <p class="product-desc">Shave Lotion Rather<br>Than Shave Cream<br>For Her</p>
    <p class="scent-name">Classic<br>Silken</p>
  </section>

  <p class="fill-weight">16 Fl. Oz. (480ml) ℮</p>

  <section class="block benefits">
    <p>Specially formulated with skin soothing ingredients to provide a smooth and effortless shave. Protects and nourishes from irritation and razor cuts. Helps prevent embarrassing shave rashes and ingrown hairs..</p>
    <p>Designed for sensitive and intimate skin. Perfect for intimate areas, legs, underarms, face, and body. Enhanced with hair and skin moisturizing agents.</p>
    <p>Can also be used to condition skin and hair after shampoo.</p>
  </section>

  <p class="block directions">Apply intimate shave cream where desired and glide razor over skin for smooth results</p>

  <p class="block scent-note">an array of light florals with a hint of baby powder</p>

  <p class="part-info">UnAssigned<br>Model: VK584731<br>SKU: VK584731</p>
</main>
</body>
</html>
```